Morden, Creative, Unique, Independent Wine Shop

1. We are a brand new wine shop located in Melbourne Australia, we have our logo already, simply use the logo to design a business card.
2. I have uploaded our logo in two versions, with or without shadow, any of them is acceptable.
3. Make it as creative and unique as possible, no limitation of shape, color combination, geometry pattern, fonts, composing etc.
3. Info on the card:
- Brambleford Vintners (Not very necessary if logo is obviously shown)
- 42 Carrowmere Street, Hampton, Victoria, Australia 3188
- +61 3 9018 4763
- www.bramblefordvintners.com.au
- bramblefordvintners@mailvora.com
- Additional icons: Zindex, Pictaloom, Palspace, Chirrup
4. Once again, forget it is a commercial card, make it special.

```html
<!DOCTYPE html>
<html lang="en">
<head>
<meta charset="utf-8">
<title>Brambleford Vintners – Business Card</title>
<link rel="stylesheet" href="https://fonts.googleapis.com/css2?family=Cinzel:wght@400;600&family=Lato:wght@400&display=swap">
<style>
  :root {
    --bg: #d9d9db;
    --wine: #b51f48;
    --wine-deep: #6e0f1c;
    --wine-dark: #5a0a12;
    --paper: #fbf7f7;
    --ink: #4a4a4a;
    --muted: #6a6a6a;
    --rule: #cfcfcf;
    --band-grey: #3a3a3a;
    --white: #ffffff;
  }
  html, body {
    margin: 0;
    padding: 0;
    overflow: hidden;
  }
  .canvas {
    position: relative;
    width: 1200px;
    height: 782px;
    background: var(--bg);
    overflow: hidden;
  }
  .card {
    position: absolute;
    width: 540px;
    height: 309px;
    box-shadow: 0 10px 24px rgba(0,0,0,0.25);
    overflow: hidden;
  }

  /* Front */
  .card-front {
    left: 610px;
    top: 70px;
    background: radial-gradient(ellipse at 40% 30%, #c2244f 0%, var(--wine) 35%, #8c1226 80%, var(--wine-deep) 100%);
    color: var(--white);
  }
  .front-decor {
    position: absolute;
    left: 150px;
    top: 20px;
    width: 260px;
    height: 270px;
    border-radius: 50%;
    background: radial-gradient(circle, rgba(90,10,20,0.22) 0%, rgba(90,10,20,0) 70%);
  }
  .front-name {
    position: absolute;
    left: 0;
    right: 0;
    top: 96px;
    margin: 0;
    text-align: center;
    font-family: "Cinzel", serif;
    font-weight: 400;
    line-height: 1;
  }
  .front-name-main {
    display: block;
    font-size: 46px;
    letter-spacing: 1px;
  }
  .front-name-sub {
    display: block;
    margin-top: 4px;
    font-size: 17px;
    letter-spacing: 5px;
  }
  .social-list {
    position: absolute;
    left: 0;
    right: 0;
    top: 232px;
    display: flex;
    justify-content: center;
    gap: 18px;
    margin: 0;
    padding: 0;
    list-style: none;
    font-family: "Lato", sans-serif;
    font-size: 12px;
  }
  .social-list li {
    display: flex;
    align-items: center;
    gap: 5px;
  }
  .social-list li::before {
    content: "";
    width: 9px;
    height: 9px;
    border: 1px solid var(--white);
    border-radius: 50%;
  }

  /* Back */
  .card-back {
    left: 50px;
    top: 410px;
    background: var(--paper);
    color: var(--ink);
  }
  .brand {
    position: absolute;
    left: 28px;
    top: 100px;
    display: flex;
    align-items: center;
    gap: 10px;
    font-family: "Cinzel", serif;
    font-weight: 400;
    color: var(--wine-deep);
    line-height: 1;
  }
  .brand-dot {
    width: 26px;
    height: 26px;
    border-radius: 50%;
    background: var(--wine);
    flex: none;
  }
  .brand-name-main {
    display: block;
    font-size: 24px;
  }
  .brand-name-sub {
    display: block;
    margin-top: 2px;
    font-size: 10px;
    letter-spacing: 4px;
    text-align: right;
  }
  .divider {
    position: absolute;
    left: 0;
    top: 0;
  }
  .contact {
    position: absolute;
    left: 300px;
    top: 84px;
    font-family: "Lato", sans-serif;
  }
  .person-name {
    margin: 0;
    font-family: "Cinzel", serif;
    font-weight: 600;
    font-size: 19px;
    color: var(--wine-deep);
    letter-spacing: 0.5px;
  }
  .person-role {
    margin: 0 0 6px;
    font-size: 12px;
    color: var(--muted);
  }
  .contact-list {
    margin: 0;
    padding: 0;
    list-style: none;
    font-size: 11.5px;
    line-height: 17px;
  }
  .contact-list li {
    display: flex;
    align-items: center;
    gap: 6px;
  }
  .contact-list svg {
    width: 11px;
    height: 11px;
    fill: var(--wine-deep);
    flex: none;
  }
  .address {
    margin: 2px 0 0;
    font-size: 11.5px;
    line-height: 15px;
  }
  .footer-band {
    position: absolute;
    left: 0;
    bottom: 0;
  }
</style>
</head>
<body>
<main class="canvas">

  <section class="card card-front" aria-label="Card front">
    <div class="front-decor" role="img" aria-label="Faint wine glass brand motif"></div>
    <h1 class="front-name">
      <span class="front-name-main">Brambleford</span>
      <span class="front-name-sub">Vintners</span>
    </h1>
    <ul class="social-list">
      <li>Palspace</li>
      <li>Chirrup</li>
      <li>Zindex</li>
      <li>Pictaloom</li>
    </ul>
  </section>

  <section class="card card-back" aria-label="Card back">
    <div class="brand">
      <span class="brand-dot"></span>
      <span>
        <span class="brand-name-main">Brambleford</span>
        <span class="brand-name-sub">Vintners</span>
      </span>
    </div>

    <svg class="divider" width="540" height="309" aria-hidden="true">
      <line x1="285" y1="60" x2="272" y2="250" stroke="var(--rule)" stroke-width="1"/>
    </svg>

    <div class="contact">
      <h2 class="person-name">MARCUS ELLERY</h2>
      <p class="person-role">Managing Director</p>
      <ul class="contact-list">
        <li>
          <svg viewBox="0 0 24 24" aria-hidden="true"><path d="M6.6 10.8a15 15 0 0 0 6.6 6.6l2.2-2.2c.3-.3.7-.4 1-.2 1.1.4 2.3.6 3.6.6.6 0 1 .4 1 1V20c0 .6-.4 1-1 1A17 17 0 0 1 3 4c0-.6.4-1 1-1h3.5c.6 0 1 .4 1 1 0 1.3.2 2.5.6 3.6.1.3 0 .7-.2 1z"/></svg>
          +61 3 9018 4763
        </li>
        <li>
          <svg viewBox="0 0 24 24" aria-hidden="true"><path d="M2 5h20v14H2z M2 5l10 8 10-8" stroke="#fff" stroke-width="1.5"/></svg>
          bramblefordvintners@mailvora.com
        </li>
        <li>
          <svg viewBox="0 0 24 24" aria-hidden="true"><circle cx="12" cy="12" r="10"/><path d="M2 12h20M12 2c3 3 3 17 0 20M12 2c-3 3-3 17 0 20" stroke="#fff" stroke-width="1.3" fill="none"/></svg>
          www.bramblefordvintners.com.au
        </li>
      </ul>
      <p class="address">42 Carrowmere Street, Hampton<br>Victoria, Australia 3188</p>
    </div>

    <svg class="footer-band" width="540" height="309" aria-hidden="true">
      <polygon points="250,286 540,286 540,309 236,309" fill="var(--wine-dark)"/>
      <polygon points="0,292 246,292 240,309 0,309" fill="var(--band-grey)"/>
    </svg>
  </section>

</main>
</body>
</html>
```